Webpress site for Nonprofit | ||
Fund Raising | ||
Who we are Team Zalvoro, a 501(c)3 corporation, provides a nurturing atmosphere for the young student-athlete. Our scholars, many from challenged foundations, are given an opportunity to train and compete at an elite level while emphasizing a strong dedication to education. These programs are designed to cultivate the skills, discipline, commitment and strong character found in high achievers. An emphasis on unity, community, and teamwork serve as the epicenter for development. These virtues are necessary for our athletes to reach their highest level of personal growth, professional achievement and community leadership. |
Cutting-Edge Flashy Professional Academic Corporate Modern Elegant Service Oriented |
Black | ||
Steel | ||
left side | ||
http://www.velvetrooms.org/ | ||
http://www.harborfieldyouthgames.org/ | ||
http://www.GlintwoodHoldings.com/ | ||
Needed Tabs: Mission Sponsors Donation (piyrx) Sports Board Events |

```html
<!DOCTYPE html>
<html lang="en">
<head>
<meta charset="utf-8">
<title>Team Zalvoro</title>
<link href="https://fonts.googleapis.com/css2?family=Arvo:wght@400;700&family=Arimo:wght@400;700&family=Tinos:wght@400;700&display=swap" rel="stylesheet">
<style>
:root{
  --bg-dark:#151515;
  --bg-mid:#2e2e2e;
  --red:#e4141b;
  --red-dark:#b30d12;
  --red-deep:#8e0a0e;
  --white:#ffffff;
  --ink:#1a1a1a;
  --grey:#8a8a8a;
  --panel:#ffffff;
  --steel:#c9ccd0;
}
*{margin:0;padding:0;box-sizing:border-box}
html,body{width:1200px;height:1054px;overflow:hidden}
body{
  position:relative;
  background:radial-gradient(ellipse at 50% 40%,var(--bg-mid) 0%,var(--bg-dark) 75%);
  font-family:"Tinos",serif;color:var(--ink);
}
.abs{position:absolute}
.brand{left:92px;top:10px;display:flex;align-items:center;gap:14px;z-index:3}
.brand-mark{width:92px;height:92px;border-radius:50%;background:var(--red-dark)}
.brand-name{font-family:"Arvo",serif;font-weight:700;font-size:24px;color:var(--white)}
.social{right:118px;top:10px;display:flex;gap:26px}
.social span{width:46px;height:46px;border-radius:50%;background:var(--steel);display:block}
.phone{right:104px;top:70px;font-family:"Arimo",sans-serif;font-size:28px;color:var(--white)}
.nav{left:80px;top:117px;width:1012px;height:49px;
  background:linear-gradient(var(--red) 0%,var(--red-dark) 100%);
  display:flex;align-items:center;padding-left:60px;gap:0}
.nav a{font-family:"Arimo",sans-serif;font-size:23px;color:var(--white);text-decoration:none;
  padding:0 22px;height:49px;line-height:49px}
.nav a.active{background:var(--red-deep)}
.hero{left:80px;top:180px;width:1012px;height:383px;background:var(--panel);border-radius:14px 14px 0 0;overflow:hidden}
.hero-photo{position:absolute;left:0;top:0;width:570px;height:383px;
  background:linear-gradient(90deg,#c79a73 0%,#e6c6a6 55%,#f6ece2 85%,#ffffff 100%)}
.hero-title{position:absolute;left:565px;top:40px;width:430px;text-align:center;
  font-family:"Arvo",serif;font-weight:700;font-size:29px;line-height:34px;color:var(--red)}
.hero-text{position:absolute;left:572px;top:118px;width:420px;font-size:16px;line-height:19px;color:var(--red)}
.btn-more{position:absolute;left:757px;top:286px;width:148px;height:44px;border-radius:8px;
  background:linear-gradient(var(--red),var(--red-dark));display:flex;align-items:center;gap:8px;padding-left:10px;
  font-family:"Arimo",sans-serif;font-size:20px;color:var(--white)}
.btn-more svg{flex:none}
.welcome{left:80px;top:563px;width:694px;height:206px;background:var(--panel);padding:14px 30px}
.welcome h1{font-family:"Arvo",serif;font-weight:400;font-size:29px;color:var(--red);margin-bottom:10px}
.welcome p{font-size:15.5px;line-height:18.5px}
.events{left:777px;top:557px;width:315px;height:352px;background:var(--panel);border-radius:10px 10px 0 0;overflow:hidden}
.events h2{height:50px;background:linear-gradient(var(--red),var(--red-dark));color:var(--white);
  font-family:"Arvo",serif;font-weight:400;font-size:27px;text-align:center;line-height:50px}
.event{margin:12px 16px 0;padding-bottom:10px;border-bottom:1px solid #ddd;position:relative}
.event h3{font-family:"Arvo",serif;font-weight:400;font-size:20px;color:var(--red-dark);margin-bottom:12px}
.event p{font-size:15px;line-height:18px}
.mini-btn{display:inline-block;background:var(--red);color:var(--white);font-family:"Arimo",sans-serif;
  font-size:10px;padding:3px 6px;border-radius:3px;float:right;margin-top:2px}
.event:after{content:"";display:block;clear:both}
.blog,.testi{top:771px;height:138px;background:var(--panel);padding:6px 12px}
.blog{left:80px;width:352px;background:linear-gradient(#e9e9e9,#fff 30%)}
.testi{left:436px;width:338px;background:linear-gradient(#e9e9e9,#fff 30%)}
.col-title{font-family:"Arvo",serif;font-weight:400;font-size:22px;color:var(--red-dark);border-bottom:1px solid #ccc;padding-bottom:2px}
.meta{font-size:10px;color:var(--grey);text-align:right;margin:2px 0}
.blog h4{font-family:"Tinos",serif;font-size:18px;color:var(--red-dark)}
.blog p,.testi p{font-size:14px;line-height:17px}
.link-more{color:var(--red-dark);font-size:14px;text-align:right;display:block}
.testi p{margin-top:8px}
.sign{text-align:right;color:var(--red);font-family:"Arvo",serif;font-weight:700;font-size:17px;line-height:19px;margin-top:16px}
.footer-col{top:921px;color:var(--white)}
.footer-col h5{font-family:"Tinos",serif;font-weight:400;font-size:17px;margin-bottom:6px}
.footer-col li{list-style:none;font-size:11px;line-height:14px;margin-left:8px}
.news{left:769px;top:911px;width:323px;height:143px;background:rgba(0,0,0,.45);padding:8px 16px;color:var(--white)}
.news h5{font-family:"Tinos",serif;font-weight:400;font-size:18px;margin-bottom:8px}
.field{display:flex;align-items:center;font-family:"Arimo",sans-serif;font-size:16px;margin-bottom:8px}
.field label{width:96px}
.field span{display:block;width:180px;height:24px;background:var(--white)}
.submit{margin-left:178px;width:84px;height:26px;background:var(--red);color:var(--white);font-family:"Arimo",sans-serif;
  font-size:16px;text-align:center;line-height:26px;border-radius:3px}
</style>
</head>
<body>
<div class="abs brand"><span class="brand-mark"></span><span class="brand-name">Team Zalvoro</span></div>
<div class="abs social" aria-hidden="true"><span></span><span></span><span></span></div>
<div class="abs phone">000-Team-Zalvoro</div>

<nav class="abs nav">
  <a class="active">Home</a><a>Mission</a><a>Sponsors</a><a>Donation</a><a>Sports</a><a>Board</a><a>Events</a>
</nav>

<section class="abs hero">
  <div class="hero-photo" role="img" aria-label="Photo of a young child hugging a teddy bear"></div>
  <div class="hero-title">Thousand childrens looking forward to your charity.</div>
  <p class="hero-text">Lorem Ipsum is simply dummy text of the printing and typesetting industry. Lorem Ipsum has been the industry's standard dummy text ever since the 1500s, when an unknown printer took a galley of type and scrambled it to make a type specimen book. It has survived not only five centuries.</p>
  <div class="btn-more"><svg width="26" height="26" viewBox="0 0 26 26"><circle cx="13" cy="13" r="12" fill="#fff"/><path d="M10 7l7 6-7 6z" fill="#e4141b"/></svg>Read More</div>
</section>

<section class="abs welcome">
  <h1>Welcome to Our Website!</h1>
  <p>Lorem Ipsum is simply dummy text of the printing and typesetting industry. Lorem Ipsum has been the industry's standard dummy text ever since the 1500s, when an unknown printer took a galley of type and scrambled it to make a type specimen book. It has survive d not only five centuries, but also the leap into electronic typesetting, remaining essentially unchanged. It was popularised in the 1960s with the release of Sheetform sheets containing Lorem Ipsum a, and more recently with desktop publishing software like Quillset Composer including versions of Lorem Ipsum.</p>
</section>

<aside class="abs events">
  <h2>Upcoming Events</h2>
  <div class="event"><h3>Lorem Ipsum is simply.</h3><p>Lorem Ipsum is simply.Lorem Ipsum is simply.Lorem Ipsum is simply.Lorem I psum is simply.</p><span class="mini-btn">Read More</span></div>
  <div class="event"><h3>Lorem Ipsum is simply.</h3><p>Lorem Ipsum is simply.Lorem Ipsum is simply.Lorem Ipsum is simply.Lorem I psum is simply.</p><span class="mini-btn">Read More</span></div>
</aside>

<section class="abs blog">
  <div class="col-title">From Blog</div>
  <div class="meta">Posted By: Mx , Nov 28,2011</div>
  <h4>Lorem Ipsum is simply dummy text</h4>
  <p>Lorem Ipsum is simply dummy text of the printing and typesetting industry.</p>
  <span class="link-more">[Read More]</span>
</section>

<section class="abs testi">
  <div class="col-title">Testimonials</div>
  <p>" Lorem Ipsum is simply dummy text of the printing and typesetting industry. "</p>
  <div class="sign">No One<br>No Post</div>
</section>

<div class="abs footer-col" style="left:120px"><h5>Lorem Ipsum</h5><ul><li>Link</li><li>Link</li><li>Link</li><li>Link</li><li>Link</li><li>Link</li></ul></div>
<div class="abs footer-col" style="left:348px"><h5>Lorem Ipsum</h5><ul><li>Link</li><li>Link</li><li>Link</li><li>Link</li><li>Link</li><li>Link</li></ul></div>
<div class="abs footer-col" style="left:577px"><h5>Lorem Ipsum</h5><ul><li>Link</li><li>Link</li><li>Link</li><li>Link</li><li>Link</li><li>Link</li></ul></div>

<section class="abs news">
  <h5>Subricbe to news letter</h5>
  <div class="field"><label>Name:</label><span></span></div>
  <div class="field"><label>E-mail:</label><span></span></div>
  <div class="submit">Submit</div>
</section>
</body>
</html>
```